Business Card Design Project

Use our current logo. Clean design.

Industry/Entity Type

Business

Requirements
Must have
• Marisela DUBRANCQ
M. Law
Managing Partner

Alpenvorsa AG
Kornhalmweg 214
CH-3097 Liebefeld

M. +41 79 412 56 27
T. +41 31 928 44 10
F. +41 31 928 44 19

m.dubrancq@alpenvorsa-example.com
www.alpenvorsa-example.com

```html
<!DOCTYPE html>
<html lang="en">
<head>
<meta charset="utf-8">
<title>Alpenvorsa – Business Card</title>
<link rel="stylesheet" href="https://fonts.googleapis.com/css2?family=Open+Sans:wght@400;600;700&display=swap">
<style>
  :root {
    --canvas-bg: #e7e5e1;
    --card-bg: #ffffff;
    --ink: #2b2b2b;
    --ink-soft: #3a3a3a;
    --card-shadow: rgba(0, 0, 0, 0.18);
  }
  * { box-sizing: border-box; margin: 0; padding: 0; }
  html, body {
    width: 1200px;
    height: 960px;
    overflow: hidden;
    background: var(--canvas-bg);
    font-family: "Open Sans", Arial, sans-serif;
    color: var(--ink);
  }
  .canvas {
    position: relative;
    width: 1200px;
    height: 960px;
  }
  .card {
    position: absolute;
    left: 300px;
    width: 600px;
    height: 388px;
    background: var(--card-bg);
    box-shadow: 0 10px 30px var(--card-shadow);
    overflow: hidden;
  }
  .card--front { top: 74px; }
  .card--back { top: 498px; }

  /* Front side */
  .brand-mark {
    position: absolute;
    top: 30px;
    right: 40px;
    font-size: 17px;
    font-weight: 600;
    letter-spacing: 0.12em;
    color: var(--ink);
  }
  .person {
    position: absolute;
    left: 60px;
    top: 150px;
    line-height: 1.3;
  }
  .person__name {
    font-size: 20px;
    font-weight: 400;
    color: var(--ink-soft);
    margin-bottom: 6px;
  }
  .person__degree {
    font-size: 19px;
    font-weight: 700;
  }
  .person__role,
  .person__address {
    font-size: 15.5px;
    color: var(--ink-soft);
  }
  .contact {
    position: absolute;
    left: 360px;
    top: 166px;
    font-size: 11.5px;
    line-height: 1.55;
    color: var(--ink-soft);
  }
  .contact__list { list-style: none; }
  .contact__gap { margin-top: 2px; }
  .swoosh {
    position: absolute;
    left: 0;
    top: 0;
    width: 600px;
    height: 388px;
  }

  /* Back side */
  .card--back .brand-name {
    position: absolute;
    inset: 0;
    display: flex;
    align-items: center;
    justify-content: center;
    font-size: 54px;
    font-weight: 600;
    letter-spacing: 0.1em;
    color: var(--ink);
  }
</style>
</head>
<body>
<main class="canvas">

  <section class="card card--front" aria-label="Business card, front">
    <div class="brand-mark">ALPENVORSA</div>

    <div class="person">
      <p class="person__name">Marisela DUBRANCQ</p>
      <p class="person__degree">M. Law</p>
      <p class="person__role">Managing Partner</p>
      <p class="person__address">Alpenvorsa AG</p>
      <p class="person__address">Kornhalmweg 214</p>
      <p class="person__address">CH-3097 Liebefeld</p>
    </div>

    <ul class="contact contact__list">
      <li>M. +41 79 412 56 27</li>
      <li>T. +41 31 928 44 10</li>
      <li>F. +41 31 928 44 19</li>
      <li class="contact__gap">m.dubrancq@alpenvorsa-example.com</li>
      <li>www.alpenvorsa-example.com</li>
    </ul>

    <svg class="swoosh" viewBox="0 0 600 388" aria-hidden="true">
      <path d="M8 338 Q 300 300 590 256 Q 300 318 8 338 Z" fill="var(--ink)"/>
    </svg>
  </section>

  <section class="card card--back" aria-label="Business card, back">
    <div class="brand-name">ALPENVORSA</div>
  </section>

</main>
</body>
</html>
```